Event Newsletter for Financial Advisors

Create a newsletter that only goes out to our field financial advisors.

Creating awareness around upcoming events, highlighting past events with pictures/video, and linking registrations to the newsletter.

```html
<!DOCTYPE html>
<html lang="en">
<head>
<meta charset="utf-8">
<title>Financial Advisors – Event Newsletter</title>
<link rel="stylesheet" href="https://fonts.googleapis.com/css2?family=Montserrat:wght@400;500;600;700&family=Oswald:wght@600;700&display=swap">
<style>
  :root {
    --rust: #a8612f;
    --rust-dark: #8c4f25;
    --charcoal: #3d3e42;
    --ink: #1f1f22;
    --black: #000000;
    --white: #ffffff;
    --text: #3a3a3a;
  }
  * { box-sizing: border-box; margin: 0; padding: 0; }
  html, body { width: 1200px; height: 4840px; overflow: hidden; background: var(--white); }
  body { font-family: "Montserrat", sans-serif; color: var(--text); position: relative; }

  .hero { position: absolute; left: 0; top: 0; width: 1200px; height: 886px;
    background: linear-gradient(180deg, #6f6a63 0%, #57524c 40%, #3f3c39 75%, #2f2d2c 100%); }
  .topbar { position: absolute; left: 0; top: 0; width: 1200px; height: 105px; background: rgba(60,60,62,0.72); }
  .brand { position: absolute; left: 120px; top: 30px; font-weight: 700; font-size: 36px; color: var(--white); letter-spacing: 0.5px; }
  .btn { display: flex; align-items: center; justify-content: center; border: 4px solid var(--rust);
    border-radius: 40px; color: var(--white); font-weight: 500; font-size: 23px; }
  .topbar .btn { position: absolute; left: 819px; top: 19px; width: 253px; height: 67px; background: #2a1f18; }
  .tagline { position: absolute; left: 124px; top: 592px; width: 950px; height: 158px;
    border: 8px solid var(--rust); background: rgba(10,10,10,0.88);
    display: flex; align-items: center; justify-content: center; text-align: center;
    color: var(--white); font-weight: 600; font-size: 34px; line-height: 52px; padding: 0 50px; }

  .about { position: absolute; left: 0; top: 886px; width: 1200px; height: 864px; background: var(--rust); }
  .section-title { font-family: "Oswald", sans-serif; font-weight: 700; text-align: center; letter-spacing: 1.5px; }
  .about .section-title { position: absolute; top: 100px; width: 100%; font-size: 52px; color: var(--white); }
  .about-copy { position: absolute; left: 124px; top: 190px; width: 952px; color: var(--white);
    font-size: 25px; line-height: 41px; text-align: justify; text-align-last: center; }
  .about-copy p + p { margin-top: 14px; }
  .about-frame { position: absolute; left: 124px; top: 1424px; width: 952px; height: 501px;
    background: var(--white); border-radius: 0 76px 0 76px; padding: 11px 11px 0 11px; }
  .about-photo { width: 920px; height: 490px; border-radius: 0 66px 0 66px;
    background: linear-gradient(120deg, #d9c6ac 0%, #b89a78 45%, #7a5a3e 100%); }

  .upcoming .section-title { position: absolute; top: 2030px; width: 100%; font-size: 60px; color: var(--ink); }
  .event-grid { position: absolute; left: 49px; top: 2141px; width: 1100px;
    display: grid; grid-template-columns: repeat(3, 351px); column-gap: 23px; row-gap: 33px; }
  .event-card { height: 160px; background: var(--rust); color: var(--white); text-align: center; padding-top: 28px; }
  .event-name { font-family: "Oswald", sans-serif; font-weight: 600; font-size: 38px; line-height: 44px; letter-spacing: 0.5px; }
  .event-date { font-weight: 700; font-size: 26px; margin-top: 6px; }
  .event-time { font-weight: 500; font-size: 19px; margin-top: 10px; }

  .past { position: absolute; left: 0; top: 2616px; width: 1200px; height: 1394px; background: var(--charcoal); }
  .past .section-title { position: absolute; top: 90px; width: 100%; font-size: 60px; color: var(--white); }
  .photo-grid { position: absolute; left: 49px; top: 201px; width: 1100px;
    display: grid; grid-template-columns: repeat(3, 351px); column-gap: 23px; row-gap: 23px; }
  .photo { height: 338px; }
  .p1 { background: linear-gradient(160deg, #a79a8c, #4c4440); }
  .p2 { background: linear-gradient(160deg, #3b3a48, #6a5a52 60%, #d8cbb6); }
  .p3 { background: linear-gradient(160deg, #2a2e4a, #2a3c7a 55%, #141830); }
  .p4 { background: linear-gradient(160deg, #c86a2c, #5a2a14 55%, #2a1810); }
  .p5 { background: linear-gradient(160deg, #8a9088, #4a4c50 60%, #2c2c30); }
  .p6 { background: linear-gradient(160deg, #d4782e, #6a3020 55%, #28202a); }
  .p7 { background: linear-gradient(160deg, #d8c29a, #8e7a66 55%, #4a3c36); }
  .p8 { background: linear-gradient(160deg, #1e2a4a, #2a3250 55%, #4a3a30); }
  .p9 { background: linear-gradient(160deg, #7a6a60, #3a3234 55%, #1e1a1c); }

  .registration .section-title { position: absolute; top: 4112px; width: 100%; font-size: 60px; color: var(--rust); }
  .reg-copy { position: absolute; left: 124px; top: 4212px; width: 952px; font-size: 25px; line-height: 41px;
    text-align: justify; text-align-last: center; color: var(--text); }
  .registration .btn { position: absolute; left: 471px; top: 4460px; width: 256px; height: 72px;
    background: var(--rust); border-color: #6e3c1a; border-width: 4px; }

  .footer { position: absolute; left: 0; top: 4620px; width: 1200px; height: 220px; background: var(--black); color: var(--white); }
  .footer-brand { position: absolute; top: 46px; width: 100%; text-align: center; font-weight: 700; font-size: 36px; letter-spacing: 0.5px; }
  .footer-rule { position: absolute; left: 0; top: 126px; width: 100%; height: 1px; background: #3a3a3a; }
  .copyright { position: absolute; top: 154px; width: 100%; text-align: center; font-size: 18px; font-weight: 500; }
</style>
</head>
<body>
  <header class="hero" role="img" aria-label="Photo of a financial advisor meeting with two clients at a table in a bright office">
    <div class="topbar">
      <div class="brand">FINANCIAL ADVISORS</div>
      <a class="btn">REGISTER NOW</a>
    </div>
    <div class="tagline">Guiding Your Financial Future with Expertise and Integrity</div>
  </header>

  <section class="about">
    <h2 class="section-title">ABOUT US</h2>
    <div class="about-copy">
      <p>Kerspiciatis unde omnis issasdte natus error sitsae voluptatem accusantium doloremque laudantium, totam resaem aperiam, eaque ipsa quae seab illo inventore veritatis et quasi architecto beatae vitae dicta sunt explicabo. Nemo enim ipsam voluptatem quia voluptas sit aspernatur</p>
      <p>Oaseotam resaem aperiam, eaque ipsa quae seab illseo inventore veritatis seet quasi architecto beatae vitae dictsesea sunt explicabo. Nemo enisesem ipsam voluptatem quia voluptas sit aspernatur.</p>
    </div>
  </section>
  <div class="about-frame">
    <div class="about-photo" role="img" aria-label="Photo of three colleagues talking on a sofa during an advisory session"></div>
  </div>

  <section class="upcoming">
    <h2 class="section-title">UPCOMING EVENTS</h2>
    <div class="event-grid">
      <div class="event-card"><div class="event-name">MARION CASTELL</div><div class="event-date">05.06.2024</div><div class="event-time">06:00 PM - 09:00 PM</div></div>
      <div class="event-card"><div class="event-name">MARION CASTELL</div><div class="event-date">05.06.2024</div><div class="event-time">06:00 PM - 09:00 PM</div></div>
      <div class="event-card"><div class="event-name">MARION CASTELL</div><div class="event-date">05.06.2024</div><div class="event-time">06:00 PM - 09:00 PM</div></div>
      <div class="event-card"><div class="event-name">MARION CASTELL</div><div class="event-date">05.06.2024</div><div class="event-time">06:00 PM - 09:00 PM</div></div>
      <div class="event-card"><div class="event-name">MARION CASTELL</div><div class="event-date">05.06.2024</div><div class="event-time">06:00 PM - 09:00 PM</div></div>
      <div class="event-card"><div class="event-name">MARION CASTELL</div><div class="event-date">05.06.2024</div><div class="event-time">06:00 PM - 09:00 PM</div></div>
    </div>
  </section>

  <section class="past">
    <h2 class="section-title">PAST EVENTS</h2>
    <div class="photo-grid">
      <div class="photo p1" role="img" aria-label="Photo of a speaker addressing a seated workshop group"></div>
      <div class="photo p2" role="img" aria-label="Photo of a presenter in front of an audience in a lecture hall"></div>
      <div class="photo p3" role="img" aria-label="Photo of a speaker on a blue-lit stage with a screen"></div>
      <div class="photo p4" role="img" aria-label="Photo of a speaker seen from behind facing a large audience"></div>
      <div class="photo p5" role="img" aria-label="Photo of an audience listening to a presenter in a seminar room"></div>
      <div class="photo p6" role="img" aria-label="Photo of a speaker with a microphone addressing a conference crowd"></div>
      <div class="photo p7" role="img" aria-label="Photo of a presenter with a microphone among a standing group"></div>
      <div class="photo p8" role="img" aria-label="Photo of a speaker on a dark stage before an audience"></div>
      <div class="photo p9" role="img" aria-label="Photo of a speaker facing a packed auditorium"></div>
    </div>
  </section>

  <section class="registration">
    <h2 class="section-title">REGISTRATION</h2>
    <p class="reg-copy">Unlock your potential and take the next step towards achieving your goals! By registering with us, you'll gain access to exclusive resources, personalized support, and expert guidance tailored to your needs. Don't miss out on the opportunity to enhance your productivity, streamline your operations, and drive your business forward.</p>
    <a class="btn">REGISTER NOW</a>
  </section>

  <footer class="footer">
    <div class="footer-brand">FINANCIAL ADVISORS</div>
    <div class="footer-rule"></div>
    <div class="copyright">©2024. All rights reserved.</div>
  </footer>
</body>
</html>
```